Property investment company needs a letterhead design!

We are a new residential and commercial property investment company. Name of the company is Morvesta Group, LLC. We have a new logo and now we need letterhead! We prefer to have a professional and upscale appearance. We don't have any fixed requirements, so be creative! Thank you for considering this project. We are so excited to see what happens!

Target Market(s)

Professional

Industry/Entity Type

Real Estate Development

```html
<!DOCTYPE html>
<html lang="en">
<head>
<meta charset="utf-8">
<title>Morvesta Group, LLC — Letterhead</title>
<link href="https://fonts.googleapis.com/css2?family=Quicksand:wght@500;600;700&family=Great+Vibes&family=Roboto:wght@400;500&display=swap" rel="stylesheet">
<style>
  :root {
    --backdrop: #1c1c1e;
    --paper: #f4f5f7;
    --paper-shade: #e3e5e9;
    --sky: #0aa6e6;
    --sky-deep: #0a86c4;
    --navy: #0b2240;
    --navy-deep: #07182f;
    --ink: #1d2330;
    --accent: #1aa3dc;
  }
  * { box-sizing: border-box; margin: 0; padding: 0; }
  html, body { width: 1200px; height: 900px; overflow: hidden; }
  body {
    background: var(--backdrop);
    display: flex; align-items: center; justify-content: center;
    font-family: "Quicksand", sans-serif;
  }
  .letterhead {
    position: relative;
    width: 620px; height: 860px;
    background: linear-gradient(135deg, var(--paper-shade) 0%, var(--paper) 55%, #fafbfc 100%);
    overflow: hidden;
    box-shadow: 0 10px 30px rgba(0,0,0,.5);
  }
  .header-band {
    position: absolute; top: 0; left: 0; right: 0; height: 112px;
    background: linear-gradient(90deg, var(--sky-deep), var(--sky));
  }
  .brand {
    position: absolute; top: 66px; left: 50%; transform: translateX(-50%);
    display: flex; align-items: center; gap: 10px;
    background: var(--paper); padding: 12px 20px; border-radius: 40px;
  }
  .brand-dot { width: 18px; height: 18px; border-radius: 50%; background: var(--navy); }
  .brand-name {
    font-weight: 700; font-size: 22px; letter-spacing: 1.5px;
    color: var(--navy); text-transform: uppercase; white-space: nowrap;
  }
  .letter-body {
    position: absolute; top: 190px; left: 78px; right: 62px;
    color: var(--ink); font-size: 10.4px; line-height: 1.62; font-weight: 500;
  }
  .recipient { margin-bottom: 6px; line-height: 1.45; }
  .salutation { margin-bottom: 4px; }
  .paragraph { text-align: justify; margin-bottom: 14px; }
  .closing { margin-top: 30px; }
  .signature {
    font-family: "Great Vibes", cursive; font-size: 24px;
    color: var(--accent); line-height: 1; margin-top: 2px;
  }
  .footer {
    position: absolute; left: 0; right: 0; bottom: 0; height: 78px;
    background: linear-gradient(90deg, var(--navy-deep), var(--navy));
    border-top: 3px solid var(--sky);
    box-shadow: 0 -5px 0 -2px var(--paper), 0 -6px 0 -2px var(--sky);
    color: #fff; font-family: "Roboto", sans-serif; font-size: 10px;
    display: flex; flex-direction: column; align-items: center; justify-content: center; gap: 6px;
  }
  .footer-row { display: flex; gap: 26px; align-items: center; }
  .contact-item { display: flex; align-items: center; gap: 5px; }
  .contact-item svg { width: 10px; height: 10px; fill: var(--sky); }
  .web-highlight { color: var(--sky); }
</style>
</head>
<body>
  <main class="letterhead">
    <div class="header-band"></div>
    <div class="brand">
      <span class="brand-dot"></span>
      <span class="brand-name">Morvesta Group, LLC</span>
    </div>

    <section class="letter-body">
      <p class="recipient">Client Name<br>Address<br>Post Box, City</p>
      <p class="salutation">Dear</p>
      <p class="paragraph">Lorem ipsum dolor sit amet, consectetur adipiscing elit. Aenean ut ipsum eget massa hendrerit vestibulum vel in velit. Donec pretium neque velit. Aliquam porta lectus nec mauris ornare venenatis. Vivamus non est turpis, et cursus sem. Mauris vehicula erat in diam auctor at bibendum nisl lacinia. Morbi imperdiet neque vehicula nunc convallis gravida. Vestibulum iaculis pretium placerat. Integer consequat, est sit amet facilisis eleifend, nibh nibh varius orci, eget dapibus arcu dui non purus. Pellentesque in magna mauris. Duis enim sapien, dictum vitae condimentum a, pulvinar vel lacus. Mauris et molestie nibh. Vestibulum vitae nulla at metus elementum porta sit amet interdum elit. Nulla sollicitudin neque eu nulla volutpat congue.</p>
      <p class="paragraph">Etiam pellentesque, velit id dapibus fermentum, turpis sapien ornare dui, ac tincidunt ligula odio congue purus. Nunc sed ante dui, in porta lectus. Cras nec sem lorem. In hac habitasse platea dictumst. Maecenas id diam quis dui porta tristique. Sed id egestas felis. Donec ullamcorper mattis posuere. Phasellus fermentum eleifend tortor vel dapibus. Vestibulum ante ipsum.</p>
      <p class="closing">Sincerely</p>
      <p class="signature">Daniel Harper</p>
    </section>

    <footer class="footer">
      <div class="footer-row">
        <span class="contact-item">
          <svg viewBox="0 0 24 24" aria-hidden="true"><path d="M6.6 10.8a15.1 15.1 0 0 0 6.6 6.6l2.2-2.2a1 1 0 0 1 1-.25 11.4 11.4 0 0 0 3.6.57 1 1 0 0 1 1 1V20a1 1 0 0 1-1 1A17 17 0 0 1 3 4a1 1 0 0 1 1-1h3.5a1 1 0 0 1 1 1c0 1.25.2 2.45.57 3.57a1 1 0 0 1-.25 1z"/></svg>
          (555) 214-0387
        </span>
        <span class="contact-item">1840 N. Alder Lane, Fairbrook, MI 49000</span>
      </div>
      <div class="footer-row">
        <span class="contact-item">
          <svg viewBox="0 0 24 24" aria-hidden="true"><path d="M2 5h20v14H2zm2 2v.5l8 5 8-5V7z"/></svg>
          MorvestaLLC@mailbox.com
        </span>
        <span class="contact-item">
          <svg viewBox="0 0 24 24" aria-hidden="true"><circle cx="12" cy="12" r="10"/></svg>
          www.<span class="web-highlight">Morvesta</span>.com
        </span>
      </div>
    </footer>
  </main>
</body>
</html>
```